Business Card Design

Take existing logo/brand and develop business card for sales team.
We have two separate brands and require a business card for each.

1. VoxHarbor
2. MyNimbusLinko

Refer to our websites www.voxharbor.example.au and www.mynimbuslinko.example.au for designs currently implemented and in the marketplace.

Both cards are brands of our parent company Quorra Systems Pty Ltd - an Australian Telecommunications company in the medium business sector. We have only business customers, no retail/residential consumers.

Target Market(s)

Australian Business - small to medium enterprise

Industry/Entity Type

Business

Contact Information for Business Card

Lev Dorrit
Sales Director
Mobile: +61 400 555 187
Direct: +61 3 9555 0137
Email: lev@voxharbor.example.au
VoxHarbor (a brand of Quorra Systems Pty Ltd)

Lev Dorrit
Sales Director
Mobile: +61 400 555 187
Direct: +61 3 9555 0137
Email: lev@mynimbuslinko.example.au
MyNimbusLinko (a brand of Quorra Systems Pty Ltd)

Font styles to use
Sans Serif
Other font styles liked:
• Roboto Condensed, Open Sans

Requirements
Must have
• Clean lines, crisp fonts - suggest Roboto Condensed or similar.
• Must be easy to read and clear.
• Brand colour #0C8CCD
• Two colour maximum
Nice to have
• Modern, intellectual and unique design.
Should not have
• No die cuts
• No copies or rip-offs of other designs

```html
<!DOCTYPE html>
<html lang="en">
<head>
<meta charset="utf-8">
<title>VoxHarbor Business Card</title>
<link rel="stylesheet" href="https://fonts.googleapis.com/css2?family=Cinzel:wght@400;600&family=Open+Sans:wght@400;600&display=swap">
<style>
  :root {
    --page: #ffffff;
    --brand-blue: #0c8ccd;
    --ink-grey: #4d4d4f;
    --card-dark: #231f20;
    --card-edge: #9a9a9a;
    --light: #ffffff;
    --shadow: rgba(0, 0, 0, 0.35);
  }
  * { margin: 0; padding: 0; box-sizing: border-box; }
  html, body {
    width: 1200px; height: 1200px; overflow: hidden;
    background: var(--page);
  }
  .board { position: relative; width: 1200px; height: 1200px; }

  .card {
    position: absolute; left: 312px; width: 552px; height: 312px;
    box-shadow: 8px 10px 12px var(--shadow);
    overflow: hidden;
  }

  /* Front */
  .card--front {
    top: 202px; background: var(--light);
    border: 1px solid var(--card-edge);
  }
  .card--front .band {
    position: absolute; left: 0; right: 0; top: 155px; bottom: 0;
    background: var(--brand-blue);
  }
  .brand {
    position: absolute; display: flex; align-items: center; gap: 8px;
  }
  .brand-dot {
    width: 48px; height: 48px; border-radius: 50%;
    background: var(--brand-blue); flex: none;
  }
  .brand-name {
    font-family: "Open Sans", sans-serif; font-weight: 400;
    font-size: 40px; letter-spacing: -0.5px; line-height: 1;
  }
  .card--front .brand { left: 54px; top: 42px; }
  .card--front .brand-name { color: var(--ink-grey); }
  .tagline {
    position: absolute; font-family: "Open Sans", sans-serif;
    font-size: 12px; color: var(--brand-blue); white-space: nowrap;
  }
  .card--front .tagline { left: 54px; top: 104px; }

  .person { position: absolute; left: 54px; top: 198px; color: var(--light); }
  .person-name {
    font-family: "Cinzel", serif; font-weight: 600; font-size: 24px;
    letter-spacing: 0.5px; line-height: 1;
  }
  .person-role {
    font-family: "Cinzel", serif; font-size: 13px; letter-spacing: 3px;
    margin-top: 9px;
  }

  .contact {
    position: absolute; right: 40px; top: 200px; color: var(--light);
    font-family: "Cinzel", serif; font-size: 13px; line-height: 18px;
    letter-spacing: 2px;
  }
  .contact-row { display: flex; }
  .contact-label { width: 20px; font-weight: 600; font-size: 14px; flex: none; }
  .contact-value { white-space: nowrap; }
  .contact-value--email { font-size: 11px; letter-spacing: 0.3px; }

  /* Back */
  .card--back { top: 620px; background: var(--card-dark); }
  .card--back .brand { left: 162px; top: 122px; }
  .card--back .brand-name { color: var(--light); }
  .card--back .tagline { left: 0; right: 0; top: 259px; text-align: center; }
</style>
</head>
<body>
<main class="board">
  <section class="card card--front" aria-label="Card front">
    <div class="brand">
      <span class="brand-dot"></span>
      <span class="brand-name">VoxHarbor</span>
    </div>
    <p class="tagline">a brand of Quorra Systems Pty Ltd</p>
    <div class="band"></div>
    <div class="person">
      <p class="person-name">Lev Dorrit</p>
      <p class="person-role">Sales Director</p>
    </div>
    <div class="contact">
      <p class="contact-row"><span class="contact-label">P</span><span class="contact-value">+61 400 555 187</span></p>
      <p class="contact-row"><span class="contact-label"></span><span class="contact-value">+61 3 9555 0137</span></p>
      <p class="contact-row"><span class="contact-label">E</span><span class="contact-value contact-value--email">LEV@VOXHARBOR.EXAMPLE.AU</span></p>
    </div>
  </section>

  <section class="card card--back" aria-label="Card back">
    <div class="brand">
      <span class="brand-dot"></span>
      <span class="brand-name">VoxHarbor</span>
    </div>
    <p class="tagline">a brand of Quorra Systems Pty Ltd</p>
  </section>
</main>
</body>
</html>
```